Bramblewick Co Leaflet. A5 2-sided Flyer for a UK Lawn Treatment Company

I need an A5 two-side leaflet / flyer designed for my Lawn Treatment company. The leaflet will be for door-drops so quick impact needed. Full colour, both sides. I provide lawn treatments to customers in the Exeter area of Devon. I would like to design to be clear, fresh and reflect the joy a good lawn and garden can bring.

Target Market(s)

Home Owners. 30-80 Years. Familys

Font styles to use
Sans Serif

Colors
9bcb3c
f78f20
ec1f27
33a6d7

Requirements
Must have
• Good front page picture
• Logo
• Contact details on front.
• Call to Action
• More details in Text file included in design.
Nice to have
• Clipart of a family / lady enjoying a lawn.

```html
<!DOCTYPE html>
<html lang="en">
<head>
<meta charset="utf-8">
<title>Bramblewick Co Leaflet</title>
<link href="https://fonts.googleapis.com/css2?family=Open+Sans:ital,wght@0,400;0,600;0,700;1,400&family=Roboto+Slab:wght@400;500&display=swap" rel="stylesheet">
<style>
  :root {
    --green-dark: #16773a;
    --green-lime: #8dc63f;
    --green-mid: #4fa83a;
    --orange: #f7931e;
    --text: #4a4a4a;
    --paper: #f3f3f2;
    --stage: #e4e4e2;
    --white: #ffffff;
  }
  * { box-sizing: border-box; margin: 0; padding: 0; }
  html, body { width: 1200px; height: 886px; overflow: hidden; }
  body { background: var(--stage); font-family: "Open Sans", sans-serif; color: var(--text); position: relative; }

  .flyer { position: absolute; top: 60px; width: 540px; height: 764px; background: var(--paper); overflow: hidden; box-shadow: 0 2px 8px rgba(0,0,0,.15); }
  .flyer--front { left: 40px; }
  .flyer--back { left: 620px; }

  .hero { position: absolute; left: 0; top: 0; width: 540px; }
  .hero--front { height: 330px; background: linear-gradient(180deg, #8a9c6e 0%, #a7b98a 30%, #6da83a 65%, #4f8f2a 100%); }
  .hero--back { height: 240px; background: linear-gradient(180deg, #9aa889 0%, #7ea35a 45%, #5c9a2f 80%, #4d8a28 100%); }

  .wave { position: absolute; left: 0; width: 540px; }
  .wave--front { top: 230px; height: 180px; }
  .wave--back { top: 150px; height: 160px; }

  .inset { position: absolute; border-radius: 50%; border: 3px solid var(--white); box-shadow: 0 0 0 2px var(--orange); background: radial-gradient(circle at 50% 35%, #7fb850 0%, #4f9a2e 55%, #2f7420 100%); }

  .brand { position: absolute; display: flex; align-items: center; gap: 10px; }
  .brand__dot { width: 16px; height: 16px; border-radius: 50%; background: var(--green-lime); }
  .brand__name { font-family: "Roboto Slab", serif; font-weight: 400; color: var(--green-dark); white-space: nowrap; }
  .brand--front { left: 0; right: 0; top: 372px; justify-content: center; }
  .brand--front .brand__name { font-size: 38px; }
  .brand--back { left: 20px; top: 250px; }
  .brand--back .brand__name { font-size: 28px; }

  .headline { position: absolute; left: 0; right: 0; top: 448px; text-align: center; font-family: "Roboto Slab", serif; font-weight: 400; color: var(--green-dark); font-size: 25px; line-height: 30px; letter-spacing: .3px; }
  .badge { position: absolute; left: 157px; top: 518px; width: 230px; height: 31px; border: 1.5px solid var(--orange); text-align: center; font-size: 15px; line-height: 28px; color: #444; }
  .claim { position: absolute; left: 0; right: 0; text-align: center; font-size: 15.5px; color: #4a4a4a; }
  .claim--years { top: 553px; }
  .claim--guarantee { top: 583px; }

  .testimonial { position: absolute; left: 34px; top: 625px; width: 473px; height: 64px; border: 1.5px solid var(--green-lime); border-radius: 6px; padding: 17px 12px 0; text-align: center; font-style: italic; font-size: 8.6px; line-height: 12.5px; color: #666; }
  .testimonial__mark { position: absolute; left: 50%; top: -14px; transform: translateX(-50%); background: var(--paper); padding: 0 5px; font-family: "Roboto Slab", serif; font-size: 30px; line-height: 26px; color: var(--green-lime); font-style: normal; }

  .footer-band { position: absolute; left: 0; bottom: 0; width: 540px; height: 48px; background: var(--green-lime); color: var(--white); font-size: 14px; text-align: center; padding-top: 20px; }
  .footer-band strong { font-weight: 700; }
  .url-pill { position: absolute; left: 110px; top: 700px; width: 320px; height: 32px; border-radius: 16px; background: var(--green-dark); color: var(--white); text-align: center; font-family: "Roboto Slab", serif; font-size: 18px; line-height: 31px; box-shadow: 0 2px 4px rgba(0,0,0,.25); z-index: 2; }

  .section { position: absolute; left: 18px; width: 505px; }
  .section__title { font-family: "Roboto Slab", serif; font-weight: 400; color: var(--green-dark); font-size: 17px; line-height: 22px; margin-bottom: 3px; }
  .section__text { font-size: 11.2px; line-height: 14px; color: #4a4a4a; }
  .section__text .cta { color: var(--green-dark); font-weight: 600; }

  .services { position: absolute; left: 18px; top: 636px; width: 510px; display: grid; grid-template-columns: 132px 142px 236px; row-gap: 4px; font-size: 11.8px; color: #444; list-style: none; }
  .services li { display: flex; align-items: center; gap: 9px; line-height: 15px; }
  .services li::before { content: "›"; display: inline-block; width: 11px; height: 11px; border-radius: 50%; background: var(--green-lime); color: var(--white); font-size: 11px; line-height: 9px; text-align: center; font-weight: 700; flex: none; }
</style>
</head>
<body>

<!-- Front side -->
<section class="flyer flyer--front">
  <div class="hero hero--front" role="img" aria-label="Photo of a smiling father and two children playing together on a lush green lawn"></div>
  <svg class="wave wave--front" viewBox="0 0 540 180" preserveAspectRatio="none" aria-hidden="true">
    <path d="M0 150 C150 120 380 115 540 50 L540 180 L0 180 Z" fill="#8dc63f"/>
    <path d="M0 175 C140 140 380 130 540 75 L540 180 L0 180 Z" fill="#4fa83a"/>
    <path d="M0 180 C80 160 120 150 190 140 C120 158 60 175 0 188 Z" fill="#f7931e"/>
    <path d="M0 180 C160 150 380 140 540 95 L540 180 Z" fill="#f3f3f2"/>
  </svg>
  <div class="inset" style="left:47px;top:218px;width:111px;height:111px" role="img" aria-label="Tree-lined striped garden lawn"></div>
  <div class="inset" style="left:213px;top:218px;width:111px;height:111px" role="img" aria-label="Close view of a neat green lawn"></div>
  <div class="inset" style="left:389px;top:218px;width:111px;height:111px" role="img" aria-label="Lawn edged with clipped shrubs"></div>

  <div class="brand brand--front"><span class="brand__dot"></span><span class="brand__name">Bramblewick Co</span></div>

  <h1 class="headline">TREATMENTS &amp; ADVICE TO KEEP YOUR<br>LAWN LOOKING NICE.</h1>
  <div class="badge">Brand new to the area!</div>
  <p class="claim claim--years">8 Years experience maintaining the finest lawns of Cheshire</p>
  <p class="claim claim--guarantee">Complete Satisfaction Guarantee!</p>

  <blockquote class="testimonial">
    <span class="testimonial__mark">&#8220;</span>
    Thank you for the lawn service you have provided over the years. It is reassuring to have you come round as I know you carried out the service as promised unlike other lawn service companies I have dealt with.<br>- Martin
  </blockquote>

  <div class="url-pill">www.bramblewickco.co.uk</div>
  <div class="footer-band">Call today on <strong>01392 555014</strong> or text <strong>07700 900123</strong> to book your lawn survey</div>
</section>

<!-- Back side -->
<section class="flyer flyer--back">
  <div class="hero hero--back" role="img" aria-label="Photo of children running and playing through a garden sprinkler on a green lawn"></div>
  <svg class="wave wave--back" viewBox="0 0 540 160" preserveAspectRatio="none" aria-hidden="true">
    <path d="M0 85 C140 40 330 45 540 20 L540 160 L0 160 Z" fill="#8dc63f"/>
    <path d="M0 118 C80 80 160 60 260 55 C160 75 80 100 0 135 Z" fill="#f7931e"/>
    <path d="M0 110 C150 65 330 70 540 45 L540 160 L0 160 Z" fill="#f3f3f2"/>
  </svg>
  <div class="inset" style="left:384px;top:158px;width:138px;height:138px" role="img" aria-label="Striped lawn with trees behind"></div>
  <div class="inset" style="left:315px;top:209px;width:111px;height:111px" role="img" aria-label="Close-up of a water droplet on a blade of grass"></div>

  <div class="brand brand--back"><span class="brand__dot"></span><span class="brand__name">Bramblewick Co</span></div>

  <div class="section" style="top:347px">
    <h2 class="section__title">For a beautiful weed-free lawn</h2>
    <p class="section__text">Call Bramblewick Co today and start your journey to a wonderful, lush, green lawn you and your family can enjoy. Arrange a no-obligation lawn survey and quotation at a time to suit you. <span class="cta">Call 01392 555014 now.</span></p>
  </div>
  <div class="section" style="top:422px">
    <h2 class="section__title">I will understand your lawn</h2>
    <p class="section__text">Every lawn is unique. I take time to gain a comprehensive understanding of your lawn and its situation. I will also listen to you and understand your problems and your aspirations for your grass.</p>
  </div>
  <div class="section" style="top:500px">
    <h2 class="section__title">Your lawn treatments</h2>
    <p class="section__text">I will create a custom treatment programme tailored to your lawn. I may also recommend some remedial treatments to correct any existing problems. There is no contract to sign. I guarantee all treatments.</p>
  </div>
  <div class="section" style="top:572px">
    <h2 class="section__title">Industry-leading lawn care</h2>
    <p class="section__text">I have 8 years of experience in the leading edge of domestic lawn care. I have a comprehensive range of treatments including:</p>
  </div>
  <ul class="services">
    <li>Scarification</li><li>Overseeding</li><li>Fertilisation &amp; Weed Control</li>
    <li>Aeration</li><li>Top Dressing</li><li>Pest and Disease Management</li>
    <li>Moss Control</li><li>Lawn Repairs</li><li>Special Event Preparation</li>
  </ul>

  <div class="url-pill">www.bramblewickco.co.uk</div>
  <div class="footer-band">Save time and money and leave your lawn to an expert. Call <strong>01392 555014</strong> Today.</div>
</section>

</body>
</html>
```